Lanterne architecture business cards

We are a new company based in New Zealand. We Specialize in High end Luxury Residential Architecture.

Every home is bespoke and is designed to each clients individual requirements and needs.

I like to design buildings that inspire people through light and form while offering a high level of comfort and usability.

Lines of sight, proportion and balance are fundamental to the spaces I create.
Updates

August 5th is current deadline - Today's date is the 13th of August.

Target Market(s)

New Zealanders who want a custom individual home design, typically 30-65 year old males and females

Industry/Entity Type

Architecture

Contact Information for Business Card

Director - Derek Tolson
Contact Number - 0279164073
Email - info@lanternearchitecture-example.co.nz
Webstie - www.lanternearchitecture-example.co.nz
Social Media - @lanternearchitecture

Font styles to use
Sans Serif

Requirements
Must have
• Logo (Both Sides)
Website
Email
Contact Number
Social Media

Nice to have
• Texture
Should not have
• More than 3 colours - typically I would've thought 2 would be good to match the logo.

```html
<!DOCTYPE html>
<html lang="en">
<head>
<meta charset="utf-8">
<title>Lanterne Architecture — Business Cards</title>
<link rel="stylesheet" href="https://fonts.googleapis.com/css2?family=Poppins:wght@300;400;600&display=swap">
<style>
  :root {
    --backdrop: #e6e6e6;
    --card: #161616;
    --card-grain: #1d1d1d;
    --ink: #ffffff;
    --ink-soft: #d9d9d9;
  }
  * { margin: 0; padding: 0; box-sizing: border-box; }
  html, body {
    width: 1200px;
    height: 800px;
    overflow: hidden;
    background: var(--backdrop);
    font-family: "Poppins", sans-serif;
  }
  .canvas {
    position: relative;
    width: 1200px;
    height: 800px;
  }
  .card {
    position: absolute;
    top: 283px;
    width: 428px;
    height: 237px;
    background:
      radial-gradient(circle at 30% 25%, var(--card-grain) 0%, transparent 60%),
      radial-gradient(circle at 75% 80%, var(--card-grain) 0%, transparent 55%),
      var(--card);
    color: var(--ink);
  }
  .card--front { left: 112px; }
  .card--back  { left: 638px; }

  /* front: brand block */
  .brand {
    position: absolute;
    left: 22px;
    top: 78px;
    width: 140px;
    text-align: center;
  }
  .brand__mark {
    display: block;
    margin: 0 auto 12px;
  }
  .brand__name {
    font-weight: 300;
    font-size: 15px;
    letter-spacing: 0.32em;
    margin-right: -0.32em;
    line-height: 1;
  }
  .brand__sub {
    margin-top: 4px;
    font-weight: 300;
    font-size: 5px;
    letter-spacing: 0.78em;
    margin-right: -0.78em;
    color: var(--ink-soft);
    line-height: 1;
  }

  /* front: contact block */
  .contact {
    position: absolute;
    right: 23px;
    top: 68px;
    text-align: right;
  }
  .contact__name {
    font-weight: 600;
    font-size: 10.5px;
    letter-spacing: 0.22em;
    margin-right: -0.22em;
    line-height: 1;
  }
  .contact__role {
    margin-top: 4px;
    font-weight: 400;
    font-size: 8.5px;
    letter-spacing: 0.28em;
    margin-right: -0.28em;
    line-height: 1;
  }
  .contact__lines {
    list-style: none;
    margin-top: 12px;
    font-weight: 300;
    font-size: 9px;
    line-height: 14px;
  }
  .contact__social {
    margin-top: 8px;
    display: flex;
    justify-content: flex-end;
    align-items: center;
    gap: 6px;
    font-weight: 300;
    font-size: 10px;
  }
  .contact__social-dot {
    width: 9px;
    height: 9px;
    border-radius: 50%;
    background: var(--ink);
  }

  /* back */
  .emblem {
    position: absolute;
    inset: 0;
    display: flex;
    flex-direction: column;
    align-items: center;
    justify-content: center;
    gap: 14px;
  }
  .emblem__name {
    font-weight: 300;
    font-size: 22px;
    letter-spacing: 0.32em;
    margin-right: -0.32em;
    line-height: 1;
  }
</style>
</head>
<body>
<main class="canvas">

  <section class="card card--front" aria-label="Business card front">
    <div class="brand">
      <svg class="brand__mark" width="26" height="26" viewBox="0 0 26 26" aria-hidden="true">
        <circle cx="13" cy="13" r="10.5" fill="none" stroke="var(--ink)" stroke-width="3"/>
      </svg>
      <div class="brand__name">LANTERNE</div>
      <div class="brand__sub">ARCHITECTURE</div>
    </div>

    <div class="contact">
      <div class="contact__name">DEREK TOLSON</div>
      <div class="contact__role">DIRECTOR</div>
      <ul class="contact__lines">
        <li>0279164073 : T</li>
        <li>info@lanternearchitecture-example.co.nz : E</li>
        <li>www.lanternearchitecture-example.co.nz : W</li>
      </ul>
      <div class="contact__social">
        <span class="contact__social-dot" aria-hidden="true"></span>
        <span>@lanternearchitecture</span>
      </div>
    </div>
  </section>

  <section class="card card--back" aria-label="Business card back">
    <div class="emblem">
      <svg width="70" height="70" viewBox="0 0 70 70" aria-hidden="true">
        <circle cx="35" cy="35" r="29" fill="none" stroke="var(--ink)" stroke-width="9"/>
      </svg>
      <div class="emblem__name">LANTERNE</div>
    </div>
  </section>

</main>
</body>
</html>
```